K5Lesson WebSite

an educational website about tutoring, client will be surfing this site looking for a tutor, please see the attached images because the contains exactly what we need.
Updates

Project Deadline Extended Reason: something went wrong with the uploaded files, we are very sorry.thank you PixelBazaar for the 5 days extension.now there is a 3 images describing the content of the three pages.good luck Added Friday, August 5, 2016

Target Market(s)

everyone

Industry/Entity Type

Education

Number of Pages Required

3 page

Font styles to use
Other font styles liked:
• something looks good in Arabic and english like "Droid Arabic Kufi"

Requirements
Must have
• the logo we attached, responsive design, simple, also try as much as you can Centering texts and layout because this website will have an Arabic version, Arabic is a Right-to-Left Language.
• a change language button,
Nice to have
• educational gestures.
• Centered texts and layout because this website will have an Arabic version, Arabic is a Right-to-Left Language.
• we have a web designer and we can download any template and add our logo and text to it, but.....
• we need creativity, so please stick to the contents in the images we attached, we need something very simple, more like a varnel home page with little touch of filtering fields like the 5 dropdownlist and the gender selection buttons.
• try not to go far away from the contents we specified in the images, use less images or dont use images at all, try not to make the client scroll down,
Should not have
• too much colors or noisy layout or heavy media

```html
<!DOCTYPE html>
<html lang="en">
<head>
<meta charset="utf-8">
<title>K5Lesson — Find a Tutor</title>
<link rel="stylesheet" href="https://fonts.googleapis.com/css2?family=Lato:wght@400;700&family=Ubuntu:wght@500;700&display=swap">
<style>
:root{
  --orange:#ff4a00;
  --orange-soft:#f47a1f;
  --blue:#2d56a6;
  --blue-nav:#3a5db0;
  --green:#7ab828;
  --sky:#4a9fce;
  --ink:#222;
  --paper:#eeeeee;
  --footer:#222222;
  --white:#ffffff;
}
*{box-sizing:border-box;margin:0;padding:0}
html,body{width:1200px;height:1170px;overflow:hidden}
body{font-family:"Lato",sans-serif;color:var(--ink);background:var(--white);position:relative}

/* header */
.site-header{position:absolute;left:0;top:0;width:1200px;height:104px;background:var(--white);border-top:2px solid var(--orange-soft)}
.brand{position:absolute;left:80px;top:34px;display:flex;align-items:center;gap:10px;font:700 36px "Lato",sans-serif;color:var(--blue)}
.brand-mark{width:34px;height:34px;background:var(--blue);border-radius:4px}
.main-nav{position:absolute;top:64px;left:455px;display:flex;font-size:14px;letter-spacing:.2px;white-space:nowrap}
.main-nav a{color:#222;text-decoration:none;padding:0 24px;border-left:1px solid #ddd;line-height:22px}
.main-nav a:first-child{border-left:0;color:var(--blue-nav)}
.home-badge{position:absolute;left:486px;top:32px;width:30px;height:22px;background:#b9c9e6;border-radius:3px}
.user-box{position:absolute;left:975px;top:25px;width:145px;height:56px;border:1px solid #ddd;border-radius:2px;box-shadow:0 1px 3px rgba(0,0,0,.1);background:#fff}
.user-avatar{position:absolute;left:10px;top:10px;width:36px;height:36px;border-radius:50%;background:linear-gradient(#9fb3c8,#5d7189);border:2px solid #dfe6ef}
.user-name{position:absolute;left:54px;top:12px;font-size:14px;font-weight:700}
.user-menu{position:absolute;left:54px;top:31px;font-size:13px;color:#555}
.user-menu::after{content:"";display:inline-block;margin-left:6px;border:4px solid transparent;border-top:5px solid var(--blue-nav);vertical-align:-1px}

/* hero */
.hero{position:absolute;left:0;top:104px;width:1200px;height:560px;background:linear-gradient(180deg,#5b4620 0%,#9a7424 25%,#c7952f 48%,#a58a4d 62%,#8f8f8f 80%,#a9a9a9 100%)}
.categories{position:absolute;left:0;top:22px;width:1200px;height:80px}
.cat{position:absolute;width:110px;margin-left:-55px;text-align:center;color:#fff;font-size:16px;font-weight:700;white-space:nowrap}
.cat-icon{width:48px;height:48px;margin:0 auto 6px;border-radius:50%;background:#d8d8d8;border:2px solid #fff;display:flex;align-items:center;justify-content:center}
.cat.active{color:var(--orange-soft)}
.cat.active .cat-icon{background:var(--orange-soft)}
.cat-sep{position:absolute;top:4px;width:1px;height:60px;background:rgba(255,255,255,.25)}

.filter-panel{position:absolute;left:80px;top:156px;width:276px;height:328px;background:var(--green);border-radius:3px}
.level-select{position:absolute;left:18px;width:240px;height:36px;background:#fff;border-radius:2px;font-size:13px;line-height:36px;padding-left:10px}
.level-select::after{content:"";position:absolute;right:10px;top:12px;border:4px solid transparent;border-bottom:5px solid #777;border-top:0}
.level-select::before{content:"";position:absolute;right:10px;top:21px;border:4px solid transparent;border-top:5px solid #777;border-bottom:0}
.gender{position:absolute;left:20px;top:250px;display:flex;gap:12px;color:#fff;font-size:14px}
.gender span::before{content:"";display:inline-block;width:7px;height:7px;border:1px solid #fff;border-radius:50%;margin-right:7px;vertical-align:1px}
.gender .on::before{border-color:var(--orange-soft);border-width:2px}
.search-btn{position:absolute;left:18px;top:278px;width:110px;height:32px;background:var(--blue);color:#fff;font-size:14px;font-weight:700;display:flex;align-items:center;justify-content:center;gap:8px;border-radius:2px}

.slider{position:absolute;left:435px;top:156px;width:685px;height:328px;border-radius:3px;overflow:hidden;box-shadow:0 2px 6px rgba(0,0,0,.25)}
.slider-photo{height:278px;background:linear-gradient(90deg,#7a3d22 0%,#a6634a 35%,#cfc8c0 60%,#e6e3df 100%)}
.slider-brand{position:absolute;left:376px;top:64px;display:flex;align-items:center;gap:8px;font:700 34px "Lato",sans-serif;color:var(--blue)}
.slider-caption{height:50px;background:var(--orange);color:#fff;font-size:24px;text-align:center;line-height:50px}

/* courses */
.courses{position:absolute;left:0;top:664px;width:1200px;height:426px;background:var(--paper)}
.course{position:absolute;top:44px;width:249px;height:329px;color:#fff;text-align:center}
.course-photo{height:169px}
.course-body{height:160px;padding-top:50px}
.course-icon{position:absolute;left:100px;top:144px;width:50px;height:50px;border-radius:50%;background:#fff;box-shadow:0 2px 4px rgba(0,0,0,.3);display:flex;align-items:center;justify-content:center}
.course h3{font:700 17px/21px "Ubuntu",sans-serif;letter-spacing:1px;padding:0 18px}
.course p{font-size:14px;line-height:18px;margin-top:7px;padding:0 20px}
.course-more{position:absolute;left:108px;top:313px;width:33px;height:33px;border-radius:50%;border:2px solid #fff;color:#fff;font-size:22px;line-height:27px}
.c-blue .course-body,.c-blue .course-more{background:var(--blue)}
.c-orange .course-body,.c-orange .course-more{background:var(--orange)}
.c-green .course-body,.c-green .course-more{background:var(--green)}
.c-sky .course-body,.c-sky .course-more{background:var(--sky)}

/* footer */
.site-footer{position:absolute;left:0;top:1090px;width:1200px;height:80px;background:var(--footer);color:#fff}
.copyright{position:absolute;left:80px;top:30px;font-size:14px}
.social{position:absolute;top:22px;width:34px;height:34px;border-radius:50%;border:2px solid #fff}
.store-badge{position:absolute;top:20px;height:39px;border:1px solid #aaa;border-radius:5px;background:#000}
</style>
</head>
<body>

<header class="site-header">
  <div class="brand"><span class="brand-mark"></span>K5Lesson</div>
  <span class="home-badge"></span>
  <nav class="main-nav">
    <a href="#">HOME</a><a href="#">FIND A TUTOR</a><a href="#">ABOUT US</a><a href="#">CONTACT US</a>
  </nav>
  <div class="user-box">
    <span class="user-avatar" role="img" aria-label="User profile photo"></span>
    <span class="user-name">Sam Rivers</span>
    <span class="user-menu">Menu</span>
  </div>
</header>

<section class="hero" role="img" aria-label="Desk scene with computer and school supplies">
  <div class="categories">
    <div class="cat active" style="left:369px"><div class="cat-icon"><svg width="26" height="20" viewBox="0 0 26 20"><path d="M13 1 1 7l12 6 12-6z" fill="#fff"/><path d="M6 10v5c4 3 10 3 14 0v-5l-7 4z" fill="#fff"/></svg></div>Academic</div>
    <span class="cat-sep" style="left:425px"></span>
    <div class="cat" style="left:469px"><div class="cat-icon"><svg width="22" height="22" viewBox="0 0 22 22"><path d="M8 3h12v13" stroke="#333" stroke-width="2.5" fill="none"/><path d="M8 3v14" stroke="#333" stroke-width="2.5"/><circle cx="5" cy="17" r="3.5" fill="#333"/><circle cx="17" cy="16" r="3.5" fill="#333"/></svg></div>Music</div>
    <span class="cat-sep" style="left:513px"></span>
    <div class="cat" style="left:557px"><div class="cat-icon"><svg width="26" height="24" viewBox="0 0 26 24"><circle cx="9" cy="15" r="6" fill="none" stroke="#333" stroke-width="4" stroke-dasharray="3 2"/><circle cx="19" cy="7" r="4" fill="none" stroke="#333" stroke-width="3" stroke-dasharray="2 2"/></svg></div>I.T.</div>
    <span class="cat-sep" style="left:602px"></span>
    <div class="cat" style="left:660px"><div class="cat-icon"><svg width="26" height="22" viewBox="0 0 26 22"><text x="1" y="19" font-family="Lato,sans-serif" font-weight="700" font-size="20" fill="#333">Aa</text></svg></div>Languages</div>
    <span class="cat-sep" style="left:720px"></span>
    <div class="cat" style="left:773px"><div class="cat-icon"><svg width="24" height="20" viewBox="0 0 24 20"><rect x="1" y="5" width="22" height="14" rx="2" fill="#333"/><rect x="8" y="1" width="8" height="5" fill="none" stroke="#333" stroke-width="2"/></svg></div>Business</div>
    <span class="cat-sep" style="left:827px"></span>
    <div class="cat" style="left:871px"><div class="cat-icon"><svg width="20" height="26" viewBox="0 0 20 26"><circle cx="12" cy="4" r="3" fill="#333"/><path d="M3 10 17 8M11 9l-2 16M10 16l6 3" stroke="#333" stroke-width="3" fill="none"/></svg></div>Dance</div>
    <span class="cat-sep" style="left:916px"></span>
    <div class="cat" style="left:960px"><div class="cat-icon"><svg width="26" height="26" viewBox="0 0 26 26"><circle cx="13" cy="13" r="11" fill="#fff" stroke="#333" stroke-width="2"/><path d="M13 9l4 3-1.5 4.5h-5L9 12z" fill="#333"/></svg></div>Sports</div>
    <span class="cat-sep" style="left:1006px"></span>
    <div class="cat" style="left:1074px"><div class="cat-icon"><svg width="26" height="26" viewBox="0 0 26 26"><circle cx="13" cy="12" r="10" fill="none" stroke="#333" stroke-width="2"/><path d="M5 8c6 0 12 3 16 9M4 14c6-2 12 0 14 7M9 3c4 4 6 10 4 18" stroke="#333" stroke-width="1.5" fill="none"/></svg></div>Arts &amp; Crafts</div>
  </div>

  <form class="filter-panel">
    <div class="level-select" style="top:22px">Level 1</div>
    <div class="level-select" style="top:66px">Level 2</div>
    <div class="level-select" style="top:111px">Level 3</div>
    <div class="level-select" style="top:155px">Level 4</div>
    <div class="level-select" style="top:200px">Level 5</div>
    <div class="gender"><span class="on">Male</span><span>Female</span><span>Both</span></div>
    <div class="search-btn">SEARCH <svg width="18" height="18" viewBox="0 0 18 18"><circle cx="7.5" cy="7.5" r="5.5" fill="none" stroke="#fff" stroke-width="2"/><path d="M11.5 11.5 16 16" stroke="#fff" stroke-width="2.4"/></svg></div>
  </form>

  <div class="slider">
    <div class="slider-photo" role="img" aria-label="Student studying at a desk beside a computer screen"></div>
    <div class="slider-brand"><span class="brand-mark"></span>K5Lesson</div>
    <div class="slider-caption">Master &amp; Phd Preperation &gt;&gt;</div>
  </div>
</section>

<section class="courses">
  <article class="course c-blue" style="left:80px">
    <div class="course-photo" role="img" aria-label="Students writing in a classroom" style="background:linear-gradient(135deg,#d9d4cc,#6f8aa6 60%,#3e5577)"></div>
    <div class="course-icon"><svg width="26" height="26" viewBox="0 0 26 26"><circle cx="13" cy="7" r="5" fill="#333"/><path d="M4 22c0-6 4-9 9-9s9 3 9 9z" fill="#333"/></svg></div>
    <div class="course-body"><h3>Spanish For Beginners To Advanced Training</h3><p>Lorem ipsum dolor sit amet, diam dollar nonummy nibh.</p></div>
    <div class="course-more">+</div>
  </article>
  <article class="course c-orange" style="left:347px">
    <div class="course-photo" role="img" aria-label="Laptop on a desk showing a web design screen" style="background:linear-gradient(135deg,#8a6a44,#3a3530 55%,#c69b5a)"></div>
    <div class="course-icon"><svg width="24" height="24" viewBox="0 0 24 24"><path d="M4 20 20 4M4 4l16 16" stroke="#333" stroke-width="3"/></svg></div>
    <div class="course-body"><h3>Become A Professional Web Designer</h3><p>Lorem ipsum dolor sit amet, diam dollar nonummy nibh.</p></div>
    <div class="course-more">+</div>
  </article>
  <article class="course c-green" style="left:613px">
    <div class="course-photo" role="img" aria-label="Photographer holding a camera" style="background:linear-gradient(135deg,#c0895e,#4a3226 55%,#a0735a)"></div>
    <div class="course-icon"><svg width="26" height="22" viewBox="0 0 26 22"><rect x="1" y="5" width="24" height="16" rx="3" fill="#333"/><rect x="8" y="1" width="10" height="5" fill="#333"/><circle cx="13" cy="13" r="5" fill="#fff"/><circle cx="13" cy="13" r="3" fill="#333"/></svg></div>
    <div class="course-body"><h3>Your Complete Guide To Photography</h3><p>Lorem ipsum dolor sit amet, diam dollar nonummy nibh.</p></div>
    <div class="course-more">+</div>
  </article>
  <article class="course c-sky" style="left:880px">
    <div class="course-photo" role="img" aria-label="Scientists working in a laboratory" style="background:linear-gradient(135deg,#a7b4be,#e4e7ea 50%,#6f7e8a)"></div>
    <div class="course-icon"><svg width="22" height="26" viewBox="0 0 22 26"><path d="M7 1h8M8 1v9L1 24h20L14 10V1" fill="none" stroke="#333" stroke-width="2"/><path d="M4 19h14l3 5H1z" fill="#333"/></svg></div>
    <div class="course-body"><h3>Medical Chemistry: The Molecular Basis</h3><p>Lorem ipsum dolor sit amet, diam dollar nonummy nibh.</p></div>
    <div class="course-more">+</div>
  </article>
</section>

<footer class="site-footer">
  <p class="copyright">Copyright © 2016 K5Lesson. All Rights Reserved</p>
  <span class="social" style="left:543px;background:#1e88d8" role="img" aria-label="Social link one"></span>
  <span class="social" style="left:589px;background:#29a9e1" role="img" aria-label="Social link two"></span>
  <span class="social" style="left:634px;background:#d63b2a" role="img" aria-label="Social link three"></span>
  <span class="store-badge" style="left:845px;width:133px" role="img" aria-label="App download badge"></span>
  <span class="store-badge" style="left:992px;width:128px" role="img" aria-label="App download badge"></span>
</footer>

</body>
</html>
```